brivox new business card design project

we need a new business card design. you can view info about us @ brivox.com. i have attached an example of our previous card with our previous name that we no longer use. We really liked the design, colors etc. look below to see more info about this project. it asks for a limited number of words. please see our website for more info about our compnay.

Target Market(s)

law enforcement

Contact Information for Business Card

i have uploaded an example of what we used before that we liked.

Font styles to use
Serif

```html
<!DOCTYPE html>
<html lang="en">
<head>
<meta charset="utf-8">
<title>Brivox Business Card</title>
<link href="https://fonts.googleapis.com/css2?family=Open+Sans:wght@400;600;700&family=Roboto:wght@500&family=Jura:wght@300&display=swap" rel="stylesheet">
<style>
  :root {
    --page: #e9e6e2;
    --night: #04141f;
    --night-glow: #0d3a52;
    --map-teal: #2a8fb0;
    --brand-blue: #2577c0;
    --band-blue: #1479bd;
    --ink-dark: #0a0f16;
    --white: #ffffff;
  }
  * { box-sizing: border-box; margin: 0; padding: 0; }
  html, body {
    width: 1200px; height: 1200px; overflow: hidden;
    background: var(--page);
  }
  .card {
    position: absolute;
    left: 290px;
    width: 580px;
    height: 330px;
    overflow: hidden;
    box-shadow: 0 6px 18px rgba(0,0,0,0.18);
  }
  /* Front */
  .card-front { top: 188px; background: var(--night); }
  .network-map {
    position: absolute;
    left: 56px; top: 40px;
    width: 461px; height: 246px;
    border-radius: 40% 30% 45% 35% / 30% 25% 55% 50%;
    background:
      radial-gradient(circle at 50% 78%, rgba(70,200,190,0.55), transparent 22%),
      radial-gradient(ellipse at 50% 45%, rgba(42,143,176,0.45), rgba(13,58,82,0.35) 60%, transparent 78%);
  }
  .front-wordmark {
    position: absolute;
    left: 0; right: 0; top: 118px;
    text-align: center;
    font-family: "Jura", sans-serif;
    font-weight: 300;
    font-size: 78px;
    letter-spacing: 6px;
    color: var(--white);
    line-height: 1;
  }
  .front-swoosh { position: absolute; left: 0; bottom: 0; width: 580px; height: 40px; }
  .front-url {
    position: absolute;
    right: 60px; bottom: 4px;
    font-family: "Open Sans", sans-serif;
    font-weight: 700;
    font-size: 22px;
    color: var(--white);
  }
  /* Back */
  .card-back { top: 579px; background: var(--brand-blue); }
  .gear-texture {
    position: absolute;
    right: 0; top: 0;
    width: 170px; height: 190px;
    background: radial-gradient(ellipse at 60% 40%, rgba(255,255,255,0.05), transparent 70%);
  }
  .back-wordmark {
    position: absolute;
    left: 44px; top: 40px;
    font-family: "Jura", sans-serif;
    font-weight: 300;
    font-size: 55px;
    letter-spacing: 4px;
    color: var(--white);
    line-height: 1;
  }
  .person {
    position: absolute;
    right: 37px; top: 167px;
    text-align: right;
  }
  .person-name {
    display: inline-block;
    font-family: "Roboto", sans-serif;
    font-weight: 500;
    font-size: 24px;
    color: var(--white);
    border-bottom: 2px solid var(--ink-dark);
    line-height: 1.15;
  }
  .person-role {
    font-family: "Open Sans", sans-serif;
    font-weight: 600;
    font-size: 13px;
    color: var(--white);
    margin-top: 4px;
    letter-spacing: 0.3px;
  }
  .edge-tab {
    position: absolute;
    right: 0; top: 170px;
    width: 13px; height: 43px;
    background: var(--white);
  }
  .contact {
    position: absolute;
    top: 258px;
    font-family: "Open Sans", sans-serif;
    font-weight: 600;
    font-size: 16px;
    line-height: 21px;
    color: var(--white);
  }
  .contact-left { left: 43px; }
  .contact-right { right: 37px; text-align: right; }
</style>
</head>
<body>
  <section class="card card-front">
    <div class="network-map" role="img" aria-label="Glowing network map of the United States with connected points of light"></div>
    <div class="front-wordmark">BRIVOX</div>
    <svg class="front-swoosh" viewBox="0 0 580 40" preserveAspectRatio="none" aria-hidden="true">
      <path d="M0 40 Q120 12 420 4 L580 6 L580 40 Z" fill="#ffffff"/>
      <path d="M90 40 Q200 10 420 7 L580 8 L580 40 Z" fill="#04141f"/>
      <path d="M120 40 Q230 16 440 11 L580 10 L580 40 Z" fill="#1479bd"/>
    </svg>
    <div class="front-url">www.brivox.com</div>
  </section>

  <section class="card card-back">
    <div class="gear-texture" role="img" aria-label="Faint gear pattern decoration"></div>
    <div class="back-wordmark">BRIVOX</div>
    <div class="person">
      <div class="person-name">Jordan Ellis</div>
      <div class="person-role">FOUNDER</div>
    </div>
    <div class="edge-tab"></div>
    <div class="contact contact-left">800.555.0142<br>info@brivox.com</div>
    <div class="contact contact-right">2418 Larkfield Avenue<br>Millbrook, TX 75990</div>
  </section>
</body>
</html>
```